Animal Eye Clinic needs a Business card

We are a new veterinary ophthalmology practice (Tessaly Animal Eye Care) and we need a business card designed. We only see animal eyes - we are not a regular veterinary clinic. We already have a logo. We are looking for a professional, good looking business card to hand out to our clients. We are looking for something simple but professional and contemporary. Our logo is likely the only picture/graphic that needs to be on the card.
Updates

Contact Information for Business Card

Marisol Dunkley, BVSc, DVM, MVSc, DECVO
Veterinary Ophthalmologist

Phone: 778.418.3097
Email: tessalyanimaleyecare@mailbrook.net
Website: tessalyanimaleyecare.net
Address: 1840 Pellworth Rd
Brenmoor, BC, V4T 8M3

Colors

Designer to choose colors to be used in the design.

Requirements
Must have
• Our logo (attached)

```html
<!DOCTYPE html>
<html lang="en">
<head>
<meta charset="utf-8">
<title>Tessaly Animal Eye Care – Business Card</title>
<link rel="stylesheet" href="https://fonts.googleapis.com/css2?family=Open+Sans:wght@300;400;600;700&display=swap">
<style>
  :root {
    --backdrop: #d6d6d6;
    --card: #050505;
    --teal: #1ba6c6;
    --white: #f4f4f4;
    --divider: #8a8a8a;
    --faint: #0b0d1c;
  }
  * { margin: 0; padding: 0; box-sizing: border-box; }
  html, body { width: 1200px; height: 2303px; overflow: hidden; }
  body {
    background: var(--backdrop);
    font-family: "Open Sans", Arial, sans-serif;
    color: var(--white);
  }
  .card-stack {
    position: absolute;
    left: 91px;
    top: 545px;
    display: flex;
    flex-direction: column;
    gap: 46px;
  }
  .card {
    position: relative;
    width: 1018px;
    height: 590px;
    background: var(--card);
    box-shadow: 14px 16px 22px rgba(0,0,0,0.45);
    overflow: hidden;
  }
  .brand {
    position: absolute;
    left: 0; right: 0;
    top: 100px;
    display: flex;
    justify-content: center;
    align-items: center;
    gap: 20px;
  }
  .brand-dot {
    width: 60px; height: 60px;
    border-radius: 50%;
    background: var(--teal);
  }
  .brand-name {
    color: var(--teal);
    font-weight: 600;
    font-size: 40px;
    line-height: 1;
  }

  .front .title {
    position: absolute; left: 0; right: 0; top: 232px;
    text-align: center;
  }
  .title-role {
    font-weight: 300;
    font-size: 58px;
    line-height: 1.1;
    letter-spacing: 1px;
  }
  .title-specialty {
    color: var(--teal);
    font-weight: 700;
    font-size: 56px;
    line-height: 1.25;
    letter-spacing: 3px;
  }
  .title-name {
    margin-top: 18px;
    font-weight: 400;
    font-size: 30px;
    letter-spacing: 0.5px;
  }
  .front .website {
    position: absolute; left: 0; right: 0; top: 505px;
    text-align: center;
    color: var(--teal);
    font-size: 22px;
    font-weight: 400;
    letter-spacing: 0.5px;
  }
  .front .website b { font-weight: 700; }

  .back-mark {
    position: absolute;
    left: 330px; top: 60px;
    width: 360px; height: 360px;
    border-radius: 50%;
    background: var(--faint);
  }
  .contact {
    position: absolute;
    top: 312px;
    left: 0; right: 0;
    display: grid;
    grid-template-columns: 500px 2px 1fr;
  }
  .contact-col {
    display: flex; flex-direction: column; gap: 22px;
    font-size: 19px; font-weight: 600;
  }
  .contact-col.left { align-items: flex-end; padding-right: 26px; }
  .contact-col.right { padding-left: 26px; }
  .contact-divider { border-left: 2px dotted var(--divider); height: 96px; margin-top: 2px; }
  .contact-item { display: flex; align-items: center; gap: 16px; height: 28px; white-space: nowrap; }
  .icon { width: 20px; height: 20px; flex: none; }
</style>
</head>
<body>
  <main class="card-stack">
    <section class="card front">
      <div class="brand">
        <div class="brand-dot"></div>
        <p class="brand-name">Tessaly Animal Eye Care</p>
      </div>
      <div class="title">
        <p class="title-role">VETERINARY</p>
        <p class="title-specialty">OPHTHALMOLOGIST</p>
        <p class="title-name">Marisol Dunkley, BVSc, DVM, MVSc, DECVO</p>
      </div>
      <p class="website">www.<b>tessalyanimaleyecare</b>.net</p>
    </section>

    <section class="card back">
      <div class="back-mark"></div>
      <div class="brand">
        <div class="brand-dot"></div>
        <p class="brand-name">Tessaly Animal Eye Care</p>
      </div>
      <div class="contact">
        <div class="contact-col left">
          <div class="contact-item">778.418.3097
            <svg class="icon" viewBox="0 0 24 24" fill="var(--teal)"><path d="M6.6 10.8c1.4 2.8 3.8 5.1 6.6 6.6l2.2-2.2c.3-.3.7-.4 1-.2 1.1.4 2.3.6 3.6.6.6 0 1 .4 1 1V20c0 .6-.4 1-1 1C10.6 21 3 13.4 3 4c0-.6.4-1 1-1h3.5c.6 0 1 .4 1 1 0 1.3.2 2.5.6 3.6.1.3 0 .7-.2 1z"/></svg>
          </div>
          <div class="contact-item">www.tessalyanimaleyecare.net
            <svg class="icon" viewBox="0 0 24 24"><circle cx="12" cy="12" r="10" fill="var(--teal)"/><path d="M2 12h20M12 2c3 3 3 17 0 20M12 2c-3 3-3 17 0 20" stroke="var(--card)" stroke-width="1.4" fill="none"/></svg>
          </div>
        </div>
        <div class="contact-divider"></div>
        <div class="contact-col right">
          <div class="contact-item">
            <svg class="icon" viewBox="0 0 24 24"><circle cx="12" cy="12" r="10" fill="none" stroke="var(--teal)" stroke-width="2.4"/><rect x="7" y="8.5" width="10" height="7" fill="var(--teal)"/><path d="M7 8.5l5 4 5-4" stroke="var(--card)" stroke-width="1.2" fill="none"/></svg>
            tessalyanimaleyecare@mailbrook.net
          </div>
          <div class="contact-item">
            <svg class="icon" viewBox="0 0 24 24" fill="var(--teal)"><path d="M12 2a7 7 0 0 0-7 7c0 5 7 13 7 13s7-8 7-13a7 7 0 0 0-7-7zm0 9.5A2.5 2.5 0 1 1 12 6.5a2.5 2.5 0 0 1 0 5z"/></svg>
            1840 Pellworth Rd Brenmoor, BC, V4T 8M3
          </div>
        </div>
      </div>
    </section>
  </main>
</body>
</html>
```